Clinical psychologist - Psychotherapist business card

Hi everyone, I'm a clinical psychologist and psychotherapist, and I’m looking for a logo for my business card. The front will feature only the logo, while the back will include my contact details (and possibly a subtle touch of the logo). I've found two logos that I like, but the first one feels a bit childish—it lacks professionalism and doesn’t stand out from other similar designs. The second one, which I do like, unfortunately gives off a clinical, impersonal vibe.

Feel free to improvise—you don’t need to base the design on the logos I previously mentioned.

I generally prefer minimalistic designs that convey warmth, trust, and professionalism. I’d also like the card to have a bright background to make it feel inviting.

Additionally, I’m leaning toward using letterpress for the print technique, so the design should be compatible with that style—elegant, tactile, and clean. However, I’m still open to other options if they better suit the design.

UPDATE: I'm considering naming my business “Velmora” (top-level domain: .gr), so you could incorporate that as well.

Target Market(s)

Psychology clients, Psychiatrists, Social media users

Industry/Entity Type

Clinical psychologist - Psychotherapist

Contact Information for Business Card

To be added later on

Colors

Designer to choose colors to be used in the design.

Requirements
Nice to have
• Possibly my initials on the front side. They are Δ Κ (capital letters) or δ κ (small letters).
Should not have
• Portraits of famous psychologists

```html
<!DOCTYPE html>
<html lang="en">
<head>
<meta charset="utf-8">
<title>Velmora – Business Card</title>
<link href="https://fonts.googleapis.com/css2?family=Gelasio:wght@400;600;700&family=Montserrat:wght@500;700&display=swap" rel="stylesheet">
<style>
  :root{
    --stage:#3b4040;
    --teal:#0c7275;
    --teal-deep:#075f62;
    --teal-soft:#0f7b7e;
    --paper:#f4f4f3;
    --paper-tone:#ebebea;
    --silver:#eef2f2;
    --ink:#0b6a6c;
  }
  *{margin:0;padding:0;box-sizing:border-box}
  html,body{width:1200px;height:1200px;overflow:hidden;background:var(--stage)}
  .stage{position:relative;width:1200px;height:1200px}
  .card{position:absolute;left:150px;width:900px;height:514px;border-radius:22px;overflow:hidden;box-shadow:0 18px 40px rgba(0,0,0,.35)}
  .card--front{top:60px;background:var(--teal)}
  .card--back{top:626px;background:var(--paper)}
  .card__texture{position:absolute;inset:0}
  .card--front .card__texture{background:radial-gradient(ellipse at 50% 40%,var(--teal-soft),var(--teal-deep))}
  .card--back .card__texture{background:linear-gradient(135deg,var(--paper),var(--paper-tone))}

  /* front */
  .front-lockup{position:absolute;left:0;right:0;top:110px;text-align:center;color:var(--silver)}
  .brand-mark{display:inline-flex;align-items:center;gap:22px}
  .brand-mark__dot{width:74px;height:74px;border-radius:50%;border:3px solid var(--silver)}
  .brand-mark__name{font-family:"Gelasio",serif;font-weight:700;font-size:74px;letter-spacing:1px}
  .tagline{display:flex;align-items:center;justify-content:center;gap:16px;margin-top:26px}
  .tagline__rule{display:flex;align-items:center;width:150px}
  .tagline__rule::before{content:"";width:8px;height:8px;border-radius:50%;background:currentColor}
  .tagline__rule::after{content:"";flex:1;height:2px;background:currentColor}
  .tagline__rule--right{flex-direction:row-reverse}
  .tagline__text{font-family:"Gelasio",serif;font-size:32px;letter-spacing:1px}
  .initials{position:absolute;left:0;right:0;bottom:70px;text-align:center;font-family:"Gelasio",serif;font-size:26px;letter-spacing:8px;color:var(--silver);opacity:.8}

  /* back */
  .back-brand{position:absolute;left:56px;top:44px;display:flex;align-items:center;gap:14px;color:var(--ink)}
  .back-brand__dot{width:34px;height:34px;border-radius:50%;border:2px solid var(--ink)}
  .back-brand__name{font-family:"Gelasio",serif;font-weight:700;font-size:30px}
  .back-brand__role{font-family:"Gelasio",serif;font-size:16px;margin-top:-2px}
  .intro{position:absolute;left:56px;top:128px;font-family:"Gelasio",serif;font-weight:700;font-size:32px;color:var(--ink)}
  .feature{position:absolute;left:0;right:0;top:205px;text-align:center;color:var(--ink);font-family:"Gelasio",serif}
  .feature__name{font-weight:700;font-size:66px;line-height:1}
  .feature__note{font-weight:600;font-size:24px;margin-top:10px}
  .contact{position:absolute;left:56px;right:56px;bottom:50px;display:flex;align-items:center;justify-content:space-between;color:var(--ink);font-family:"Montserrat",sans-serif}
  .contact__title{font-weight:700;font-size:24px;letter-spacing:1px}
  .contact__item{display:flex;align-items:center;gap:12px;font-weight:500;font-size:22px}
  .contact__icon{width:30px;height:30px}
</style>
</head>
<body>
<main class="stage">

  <section class="card card--front" aria-label="Card front">
    <div class="card__texture" role="img" aria-label="Faint repeating brand pattern on teal"></div>
    <div class="front-lockup">
      <div class="brand-mark">
        <span class="brand-mark__dot"></span>
        <span class="brand-mark__name">Velmora</span>
      </div>
      <div class="tagline">
        <span class="tagline__rule"></span>
        <span class="tagline__text">Psychotherapist</span>
        <span class="tagline__rule tagline__rule--right"></span>
      </div>
    </div>
    <div class="initials">Δ Κ</div>
  </section>

  <section class="card card--back" aria-label="Card back">
    <div class="card__texture" role="img" aria-label="Faint repeating brand pattern on white"></div>
    <div class="back-brand">
      <span class="back-brand__dot"></span>
      <div>
        <div class="back-brand__name">Velmora</div>
        <div class="back-brand__role">Psychotherapist</div>
      </div>
    </div>
    <p class="intro">I'm a clinical psychologist and psychotherapist</p>
    <div class="feature">
      <div class="feature__name">“Velmora”</div>
      <div class="feature__note">(top-level domain: .gr)</div>
    </div>
    <div class="contact">
      <span class="contact__title">CONTACT US</span>
      <span class="contact__item">
        <svg class="contact__icon" viewBox="0 0 24 24" fill="none" stroke="currentColor" stroke-width="1.8" stroke-linecap="round" stroke-linejoin="round"><path d="M5 4h4l2 5-2.5 1.5a11 11 0 0 0 5 5L15 13l5 2v4a2 2 0 0 1-2 2A16 16 0 0 1 3 6a2 2 0 0 1 2-2"/></svg>
        +30 210 555 0147
      </span>
      <span class="contact__item">
        <svg class="contact__icon" viewBox="0 0 24 24" fill="none" stroke="currentColor" stroke-width="1.8"><circle cx="12" cy="12" r="9"/><path d="M3 12h18M12 3c3 3 3 15 0 18M12 3c-3 3-3 15 0 18"/></svg>
        www.velmora.gr
      </span>
    </div>
  </section>

</main>
</body>
</html>
```